The Velvet Magpie business card

I need a business card for my makeup artist business. I specialise in bridal, glamour, formal and special occasion makeup.
I am a mobile makeup artist who caters for every from nowra to sydney.
I do the following services:
Bridal makeup
airbrush makeup
special occasion
formals
hens nights/ girls night
makeup lesson
makeup for all ages from flower girl to Nanna of the bride!
photoshoot makeup
SPFX

I would like the card to portray a very professional sleek makeup business. I would also like another version of the card directed especially towards brides.

Please see my website to understand colours etc www.thevelvetmagpie.com

The Velvet Magpie
Professional Makeup Artist
Marisol Dunkel
0471829304
info@thevelvetmagpie.com
www.thevelvetmagpie.com
www.facebook.com/thevelvetmagpie

```html
<!DOCTYPE html>
<html lang="en">
<head>
<meta charset="utf-8">
<title>The Velvet Magpie – Business Card</title>
<link rel="stylesheet" href="https://fonts.googleapis.com/css2?family=Oswald:wght@300;400&family=Open+Sans:wght@400;600&display=swap">
<style>
  :root {
    --magenta: #e0197f;
    --magenta-soft: #f06aa8;
    --magenta-pale: #f8c3dc;
    --ink: #2b2b2b;
    --paper: #ffffff;
    --backdrop: #e9e7e4;
    --lash: #1e1e1e;
  }
  * { box-sizing: border-box; margin: 0; padding: 0; }
  html, body {
    width: 1200px; height: 871px; overflow: hidden;
    background: var(--backdrop);
  }
  .canvas {
    position: relative; width: 1200px; height: 871px;
    display: flex; justify-content: center; align-items: center; gap: 70px;
  }
  .card {
    position: relative; width: 440px; height: 770px;
    box-shadow: 0 6px 22px rgba(0,0,0,.18);
    overflow: hidden;
  }

  /* Front */
  .card-front { background: var(--paper); }
  .floral-top {
    position: absolute; top: 0; right: 0; width: 230px; height: 150px;
    background: radial-gradient(ellipse at 70% 40%, var(--magenta-soft) 0%, var(--magenta-pale) 55%, rgba(255,255,255,0) 75%);
  }
  .floral-bottom {
    position: absolute; left: 0; bottom: 0; width: 100%; height: 210px;
    background: radial-gradient(ellipse at 50% 75%, var(--magenta-soft) 0%, var(--magenta-pale) 50%, rgba(255,255,255,0) 75%);
  }
  .brand-rule {
    position: absolute; top: 108px; left: 0; width: 330px; height: 8px;
    background: var(--magenta);
  }
  .brand-name {
    position: absolute; top: 138px; left: 58px;
    font-family: "Oswald", sans-serif; font-weight: 300;
    font-size: 38px; letter-spacing: 5px; text-transform: uppercase;
    color: var(--magenta);
  }
  .person { position: absolute; top: 268px; left: 58px; }
  .person-name {
    font-family: "Open Sans", sans-serif; font-size: 25px; color: var(--ink);
  }
  .person-title {
    font-family: "Open Sans", sans-serif; font-size: 16px; color: var(--magenta);
    margin-top: 2px;
  }
  .contact-list { position: absolute; top: 370px; left: 58px; list-style: none; }
  .contact-list li {
    display: flex; align-items: center; gap: 12px; height: 30px;
    font-family: "Open Sans", sans-serif; font-size: 17px; color: var(--ink);
  }
  .contact-icon { width: 20px; height: 20px; flex: none; }

  /* Back */
  .card-back { background: var(--magenta); color: var(--paper); }
  .services-heading {
    position: absolute; top: 44px; left: 0; padding-left: 22px;
    border-left: 8px solid var(--paper);
    font-family: "Oswald", sans-serif; font-weight: 400; font-size: 26px;
    letter-spacing: .5px; line-height: 36px;
  }
  .services-list {
    position: absolute; top: 140px; left: 50px; right: 30px; list-style: none;
    font-family: "Open Sans", sans-serif; font-size: 19px; line-height: 32px;
  }
  .services-list .indent { padding-left: 70px; }
  .services-list .gap { margin-top: 10px; }
  .visit-panel {
    position: absolute; left: 50px; right: 0; bottom: 60px; height: 120px;
    background: var(--paper); border-radius: 22px 0 0 22px;
  }
  .visit-title {
    position: absolute; top: 16px; left: 16px;
    font-family: "Oswald", sans-serif; font-weight: 400; font-size: 22px;
    color: var(--magenta);
  }
  .lash-art {
    position: absolute; top: 10px; right: 28px; width: 170px; height: 40px;
    background: linear-gradient(180deg, var(--lash) 0%, #555 100%);
    border-radius: 50% 50% 12px 12px;
  }
  .social-line {
    position: absolute; top: 66px; left: 16px; display: flex; align-items: center; gap: 12px;
    font-family: "Open Sans", sans-serif; font-size: 20px; color: var(--ink);
  }
  .social-dot { width: 22px; height: 22px; border-radius: 50%; background: var(--magenta); }
</style>
</head>
<body>
<main class="canvas">

  <section class="card card-front">
    <div class="floral-top" role="img" aria-label="Pink floral swirl ornament"></div>
    <div class="brand-rule"></div>
    <h1 class="brand-name">The Velvet Magpie</h1>

    <div class="person">
      <p class="person-name">Marisol Dunkel</p>
      <p class="person-title">Professional Makeup Artist</p>
    </div>

    <ul class="contact-list">
      <li>
        <svg class="contact-icon" viewBox="0 0 20 20"><circle cx="10" cy="10" r="10" fill="var(--magenta)"/><path d="M7 5.5c.6 0 1 .9 1.2 1.6.2.6-.6.9-.6 1.3.2 1.2 1.7 2.7 2.9 3 .5 0 .7-.8 1.3-.6.7.2 1.6.6 1.6 1.2 0 .8-1 1.6-1.9 1.5C9 13.3 6.6 10.9 5.6 8 5.3 7 6.2 5.5 7 5.5z" fill="#fff"/></svg>
        0471829304
      </li>
      <li>
        <svg class="contact-icon" viewBox="0 0 20 20"><circle cx="10" cy="10" r="10" fill="var(--magenta)"/><rect x="5" y="6.5" width="10" height="7" fill="none" stroke="#fff" stroke-width="1.3"/><path d="M5 6.8l5 4 5-4" fill="none" stroke="#fff" stroke-width="1.3"/></svg>
        info@thevelvetmagpie.com
      </li>
      <li>
        <svg class="contact-icon" viewBox="0 0 20 20"><circle cx="10" cy="10" r="10" fill="var(--magenta)"/><circle cx="10" cy="10" r="5" fill="none" stroke="#fff" stroke-width="1.2"/><ellipse cx="10" cy="10" rx="2.2" ry="5" fill="none" stroke="#fff" stroke-width="1.1"/><path d="M5 10h10" stroke="#fff" stroke-width="1.1"/></svg>
        www.thevelvetmagpie.com
      </li>
      <li>
        <svg class="contact-icon" viewBox="0 0 20 20"><circle cx="10" cy="10" r="10" fill="var(--magenta)"/></svg>
        / thevelvetmagpie
      </li>
    </ul>

    <div class="floral-bottom" role="img" aria-label="Pink floral swirl ornament with small flowers"></div>
  </section>

  <section class="card card-back">
    <h2 class="services-heading">OUR SERVICES</h2>
    <ul class="services-list">
      <li>Bridal Makeup</li>
      <li>Airbrush Makeup</li>
      <li>Special Occasion</li>
      <li>Formals</li>
      <li>Hens Nights/ Girls Night</li>
      <li>Makeup Lesson</li>
      <li>Makeup For All Ages From Flower Girl</li>
      <li class="indent">To Nanna Of The Bride!</li>
      <li class="gap">Photoshoot Makeup</li>
      <li>Spfx</li>
    </ul>

    <div class="visit-panel">
      <p class="visit-title">Visit Us</p>
      <div class="lash-art" role="img" aria-label="Pair of false eyelashes illustration"></div>
      <p class="social-line"><span class="social-dot"></span>/thevelvetmagpie</p>
    </div>
  </section>

</main>
</body>
</html>
```